We need a website that entices australia's workers to sign up to help protect their industry and their jobs. The key message is "Building a Stronger Australia" and that headline / tagline should feature prominently on the site.

In terms of style I lack the current 'scrolling' style (see example http://www.fieldmarkweb.ca )

The site must dynamically for mobile platforms. It must also use Quenda or Paperloft as CMS so is client editable.

The attached logo is the basis for the design and the name of the organisation is the Enduring Progress Council. Please make an allowance for an iframe embed (min height 650px) see attached sample.

It should also have a subscriber sign up for that connects with Mailbridge Relay

Attached text for front page is DRAFT ONLY

Target Market(s)

Working class australians, (eg miners, farmers, factory workers, etc)

Industry/Entity Type

Industry

Coding

Coded - Design and coding required

Number of Pages Required

4 page

Requirements
Must have
• An editable CMS
• Subscription form connecting with Mailbridge Relay (see https://kovalpint.sendquill.com/help/topic.aspx?t=13)
• Must resize for mobile
• Must allow for an iframe
Nice to have
• It must have a friendly feel but strong, not 'girly' though should not alienate women
Should not have
• Images that are not australian
• Images that do not have the appropriate rights to use

```html
<!DOCTYPE html>
<html lang="en">
<head>
<meta charset="utf-8">
<title>Enduring Progress Council — Building a Stronger Australia</title>
<link rel="stylesheet" href="https://fonts.googleapis.com/css2?family=Open+Sans:ital,wght@0,400;0,600;0,700;1,400&display=swap">
<style>
:root{
  --ink:#222;
  --grey-text:#555;
  --hero-dark:#161616;
  --hero-head:#9a9a9a;
  --orange:#f05a28;
  --orange-mid:#e8781e;
  --amber:#fbb03b;
  --teal:#137c9a;
  --teal-light:#1a9cc0;
  --paper:#f6f7f9;
  --slate:#d9d9d9;
  --panel:#101010;
  --footer:#454545;
  --footer-text:#9a9a9a;
  --white:#fff;
}
*{box-sizing:border-box;margin:0;padding:0}
html,body{width:1200px;height:2478px;overflow:hidden}
body{font-family:"Open Sans",Arial,sans-serif;color:var(--ink);position:relative;background:var(--white)}
.hero{position:absolute;top:0;left:0;width:1200px;height:490px;background:var(--hero-dark)}
.hero-photo{position:absolute;left:0;top:0;width:623px;height:490px;background:linear-gradient(135deg,#4f6b3a 0%,#8a6a52 40%,#2f8a98 75%,#1f6f86 100%)}
.hero-panel{position:absolute;left:623px;top:0;width:577px;height:490px;background:radial-gradient(circle at 70% 30%,#2a2a2a,#0d0d0d 75%);border-top:4px solid var(--orange)}
.brand{position:absolute;left:23px;top:124px;display:flex;align-items:center;gap:12px;color:var(--white);font-size:17px;font-weight:600}
.brand-dot{width:30px;height:30px;border-radius:50%;background:var(--orange)}
.hero-title{position:absolute;left:22px;top:232px;color:var(--hero-head);font-size:30px;font-weight:700;line-height:34px;text-transform:uppercase}
.hero-sub{position:absolute;left:22px;top:306px;color:#c8c8c8;font-size:34px;font-style:italic}
.hero-note{position:absolute;left:22px;top:364px;width:340px;color:#9a9a9a;font-size:15px;font-style:italic;line-height:19px}
.hero-btn{position:absolute;left:20px;top:418px;height:25px;padding:0 12px;background:var(--teal);border:1px solid var(--teal-light);color:var(--white);font-size:11px;font-weight:600;line-height:23px;text-transform:uppercase;border-radius:2px}
.nav{position:absolute;top:490px;left:0;width:1200px;height:44px;background:linear-gradient(to right,var(--orange) 0 623px,var(--amber) 623px)}
.nav a{position:absolute;top:13px;font-size:14px;font-weight:700;color:#1a1a1a;text-decoration:none}
.intro{position:absolute;top:534px;left:0;width:1200px;height:304px;background:var(--paper);text-align:center}
.intro-lead{margin-top:48px;font-size:23px;line-height:30px;color:#333}
.intro-lead b{font-weight:400;color:#111}
.c-mining{color:var(--amber)}.c-agri{color:var(--orange)}.c-ind{color:var(--teal)}
.intro-country{font-size:42px;line-height:56px;color:#111}
.intro-body{width:740px;margin:26px auto 0;font-size:14px;line-height:18px;color:var(--grey-text)}
.reasons{position:absolute;top:838px;left:0;width:1200px;height:524px;background:radial-gradient(circle at 50% 60%,#f08a2a,var(--orange-mid) 70%);color:var(--white)}
.reasons-title{position:absolute;top:50px;left:0;width:1200px;text-align:center;font-size:29px;line-height:33px;font-weight:600}
.reason-list{position:absolute;top:198px;left:208px;list-style:none}
.reason-list li{position:relative;padding-left:48px;font-size:23px;line-height:27px;font-weight:600;margin-bottom:25px;width:720px}
.reason-list svg{position:absolute;left:0;top:0}
.action{position:absolute;top:1362px;left:0;width:1200px;height:511px;background:linear-gradient(#1f1f1f,#141414)}
.form-card{position:absolute;left:400px;top:26px;width:410px;height:458px;background:var(--panel);border:1px solid #2a2a2a;border-radius:3px;padding:20px 22px}
.form-card h3{font-size:15px;font-weight:400;color:#ddd}
.form-card h3 a{color:var(--teal-light);text-decoration:none}
.form-card p{font-size:10px;line-height:15px;color:#777;margin-top:10px}
.form-card h4{font-size:11px;color:#ddd;margin-top:12px;font-weight:600}
.form-card p.small{margin-top:4px}
.field{display:block;width:345px;height:24px;margin-top:14px;border:1px solid #2c2c2c;background:#141414;color:#666;font-size:9px;line-height:22px;padding-left:12px;position:relative}
.field.first{margin-top:16px}
.field.select::after{content:"▾";position:absolute;right:10px;color:#666}
.form-actions{margin-top:22px;display:flex;gap:14px}
.form-actions span{width:82px;height:24px;background:var(--teal);border:1px solid var(--teal-light);color:var(--white);font-size:11px;text-align:center;line-height:22px;border-radius:2px}
.start{position:absolute;top:1873px;left:0;width:1200px;height:302px;background:var(--slate);text-align:center}
.start h2{margin-top:40px;font-size:32px;font-weight:400;color:var(--teal)}
.start p{width:880px;margin:14px auto 0;font-size:16.5px;line-height:24px;color:#333}
.start-btn{position:absolute;left:457px;top:187px;width:210px;height:32px;background:var(--teal);border:1px solid #0c5f77;color:var(--white);font-size:16px;line-height:30px;border-radius:2px}
.footer{position:absolute;top:2175px;left:0;width:1200px;height:303px;background:var(--footer);border-top:3px solid var(--teal-light);color:var(--footer-text)}
.footer h5{position:absolute;top:55px;font-size:12px;color:var(--white);font-weight:700}
.footer-about{position:absolute;left:210px;top:85px;width:230px;font-size:10px;line-height:14px;color:#888}
.contact-row{position:absolute;left:210px;display:flex;align-items:center;gap:16px;font-size:10px;color:#999}
.posts{position:absolute;left:466px;top:88px;list-style:none;font-size:10px;color:#ccc;line-height:20.5px}
.footer-bottom{position:absolute;left:0;top:252px;width:1200px;border-top:1px solid #555}
.copyright{position:absolute;left:210px;top:270px;font-size:10px;color:#888}
.footer-nav{position:absolute;left:675px;top:270px;font-size:10px;color:#ddd;display:flex}
.footer-nav span{padding:0 9px;border-left:1px solid #777}
.footer-nav span:first-child{border-left:0}
</style>
</head>
<body>
<header class="hero">
  <div class="hero-photo" role="img" aria-label="Photograph of a smiling Australian family of four outdoors"></div>
  <div class="hero-panel">
    <div class="brand"><span class="brand-dot"></span>Enduring Progress Council</div>
    <h1 class="hero-title">Building a stronger<br>Australia</h1>
    <div class="hero-sub">My family comes first</div>
    <p class="hero-note">I care for the environment – but not at the cost of my job, our savings or our retirement</p>
    <div class="hero-btn">Take action to protect your family</div>
  </div>
</header>
<nav class="nav">
  <a style="left:209px">Take Action</a>
  <a style="left:408px">About</a>
  <a style="left:544px">Facts</a>
  <a style="left:677px">News</a>
  <a style="left:816px">Contact</a>
</nav>
<section class="intro">
  <p class="intro-lead">The <b>Greenies</b> want your bank and your <b>super fund</b> to stop investing<br>in <span class="c-mining">mining</span>, <span class="c-agri">agriculture</span> and other <span class="c-ind">industries</span> that are the <b>backbone</b> of</p>
  <div class="intro-country">Australia</div>
  <p class="intro-body">While they are trying to ‘do good’ if they are successful their actions will severely impact the lives of everyday Australians. Any loss of investment in Australian industries WILL have knock on effects for you, your family and your community.</p>
</section>
<section class="reasons">
  <h2 class="reasons-title">Tell your bank and super fund you do NOT want them to<br>divest out of Australian industry. Tell them you want to<br>keep Australia strong</h2>
  <ul class="reason-list">
    <li><svg width="34" height="34" viewBox="0 0 34 34"><polygon points="17,2 30,9.5 30,24.5 17,32 4,24.5 4,9.5" fill="none" stroke="#fff" stroke-width="2"/><polygon points="17,9 23.5,13 23.5,21 17,25 10.5,21 10.5,13" fill="none" stroke="#fff" stroke-width="2"/></svg>Cost you your job as less investment means less jobs</li>
    <li><svg width="34" height="34" viewBox="0 0 34 34"><polygon points="17,2 30,9.5 30,24.5 17,32 4,24.5 4,9.5" fill="none" stroke="#fff" stroke-width="2"/><polygon points="17,9 23.5,13 23.5,21 17,25 10.5,21 10.5,13" fill="none" stroke="#fff" stroke-width="2"/></svg>Give you less to retire on as your superannuation fund gets strong returns from investment</li>
    <li><svg width="34" height="34" viewBox="0 0 34 34"><polygon points="17,2 30,9.5 30,24.5 17,32 4,24.5 4,9.5" fill="none" stroke="#fff" stroke-width="2"/><polygon points="17,9 23.5,13 23.5,21 17,25 10.5,21 10.5,13" fill="none" stroke="#fff" stroke-width="2"/></svg>Reduce your hard earned savings</li>
    <li><svg width="34" height="34" viewBox="0 0 34 34"><polygon points="17,2 30,9.5 30,24.5 17,32 4,24.5 4,9.5" fill="none" stroke="#fff" stroke-width="2"/><polygon points="17,9 23.5,13 23.5,21 17,25 10.5,21 10.5,13" fill="none" stroke="#fff" stroke-width="2"/></svg>Impact communities that rely on industry</li>
    <li><svg width="34" height="34" viewBox="0 0 34 34"><polygon points="17,2 30,9.5 30,24.5 17,32 4,24.5 4,9.5" fill="none" stroke="#fff" stroke-width="2"/><polygon points="17,9 23.5,13 23.5,21 17,25 10.5,21 10.5,13" fill="none" stroke="#fff" stroke-width="2"/></svg>Not help the environment at all</li>
  </ul>
</section>
<section class="action">
  <div class="form-card">
    <h3>Email your bank - it's easy, <a>Click here</a></h3>
    <p>Take a few moments to contact your bank and let them know you do not want them to divest from Australian industry. Here's your opportunity to be heard. Your voice will make a difference.</p>
    <h4>It's easy to get started</h4>
    <p class="small">We have developed an advocacy centre — a place where you can send a letter or email to your bank, super fund, MP or your newspaper, share information online with your friends via social media,.</p>
    <span class="field first">First Name</span>
    <span class="field">Family Name</span>
    <span class="field">Email</span>
    <span class="field select">Select Bank</span>
    <span class="field select">Super Fund</span>
    <div class="form-actions"><span>Submit</span><span>Cancel</span></div>
  </div>
</section>
<section class="start">
  <h2>It's easy to get started</h2>
  <p>We have developed an advocacy centre — a place where you can send a letter or email to your bank, super fund, MP or your newspaper, share information online with your friends via social media,.</p>
  <div class="start-btn">Get it Now !</div>
</section>
<footer class="footer">
  <h5 style="left:218px">About us</h5>
  <h5 style="left:466px">Latest Posts</h5>
  <h5 style="left:730px">Latest Tweets</h5>
  <p class="footer-about">We say what we do, we do what we say, and we're looking forward to prove it to you.</p>
  <div class="contact-row" style="top:138px"><svg width="14" height="16" viewBox="0 0 14 16"><path d="M7 1a5 5 0 0 0-5 5c0 4 5 9 5 9s5-5 5-9a5 5 0 0 0-5-5z" fill="#aaa"/><circle cx="7" cy="6" r="2" fill="#454545"/></svg>18 Harbour Lane, Melbourne, Australia</div>
  <div class="contact-row" style="top:168px"><svg width="14" height="16" viewBox="0 0 14 16"><path d="M3 1l3 3-2 2c1 2 3 4 5 5l2-2 3 3-2 3C6 14 1 8 1 3z" fill="#aaa"/></svg>(03) 5550 1842</div>
  <div class="contact-row" style="top:198px"><svg width="16" height="12" viewBox="0 0 16 12"><rect x="1" y="1" width="14" height="10" fill="none" stroke="#aaa" stroke-width="1.5"/><path d="M1 1l7 6 7-6" fill="none" stroke="#aaa" stroke-width="1.5"/></svg>info@enduringprogress.com.au</div>
  <ul class="posts"><li>Shortcode System</li><li>List Styles</li><li>Icons</li><li>About us</li><li>About us (2)</li><li>Offline Page</li></ul>
  <div class="footer-bottom"></div>
  <div class="copyright">© 2014 Enduring Progress Inc. All rights reserved.</div>
  <div class="footer-nav"><span>Home</span><span>Take Action</span><span>About us</span><span>Facts</span><span>News</span><span>Contact</span></div>
</footer>
</body>
</html>
```